Gutschein-Design für Verkauf von Online-Schmuckstücken
Zielgruppe
Wir verkaufen Online Schmuckstücke!
www.feldring-atelier.example
Aufgabenstellung
Wir haben eine schwarze Schachtel erstellt und da drinne wird eine Geschenkgutschein sein:
Es soll sehr schlicht sein und schwarzen Hintergrund haben.
Vorderseite nur unser LOGO.
Rückseite:
Betrag: _________
Gültig Bis: _________
Code: __________
Und unten klein gedruckt steht:
Diese Karte ist gültig nur auf der online shop seite www.feldring-atelier.example und in unserer offizielen Stores. Dieses Karte ist nicht gültig bei rabatierte Produkten und man kann nicht mit dieser karte einen Gutscheinkarte kaufen.
Der Design soll sehr schlicht und dezenz sein.

```html
<!DOCTYPE html>
<html lang="de">
<head>
<meta charset="utf-8">
<title>Gutschein – Feldring Atelier</title>
<link rel="stylesheet" href="https://fonts.googleapis.com/css2?family=Montserrat:wght@700&family=Roboto:wght@400;500&display=swap">
<style>
  :root {
    --page-bg: #262321;
    --card-bg: #221f1d;
    --card-bg-light: #2c2927;
    --card-shadow: rgba(0, 0, 0, 0.55);
    --ink-light: #ffffff;
    --ink-dark: #1d1b1a;
    --accent-pink: #e9aeb9;
  }
  * { box-sizing: border-box; margin: 0; padding: 0; }
  html, body {
    width: 1200px;
    height: 800px;
    overflow: hidden;
    background: var(--page-bg);
  }
  .canvas {
    position: relative;
    width: 1200px;
    height: 800px;
    background: radial-gradient(ellipse at 20% 10%, #3a3633 0%, var(--page-bg) 55%, #1f1c1b 100%);
  }
  .card {
    position: absolute;
    left: 220px;
    width: 760px;
    height: 340px;
    background: linear-gradient(135deg, var(--card-bg-light) 0%, var(--card-bg) 60%);
    box-shadow: 0 14px 30px var(--card-shadow);
    overflow: hidden;
  }
  .card--front { top: 40px; }
  .card--back { top: 420px; }

  .front-title {
    position: absolute;
    left: 0;
    right: 0;
    top: 112px;
    text-align: center;
    font-family: "Montserrat", sans-serif;
    font-weight: 700;
    font-size: 84px;
    letter-spacing: 1px;
    color: var(--ink-light);
  }

  .brand {
    position: absolute;
    left: 70px;
    top: 118px;
    display: flex;
    align-items: center;
    gap: 16px;
  }
  .brand-dot {
    width: 54px;
    height: 54px;
    border-radius: 50%;
    background: var(--ink-light);
  }
  .brand-name {
    font-family: "Roboto", sans-serif;
    font-weight: 400;
    font-size: 36px;
    color: var(--ink-light);
  }

  .fields {
    position: absolute;
    left: 420px;
    top: 36px;
    width: 300px;
    display: flex;
    flex-direction: column;
    gap: 14px;
  }
  .field {
    height: 58px;
    background: var(--ink-light);
    display: flex;
    align-items: center;
    padding-left: 18px;
    font-family: "Roboto", sans-serif;
    font-size: 17px;
    color: var(--ink-dark);
  }

  .terms {
    position: absolute;
    left: 40px;
    right: 40px;
    bottom: 26px;
    text-align: center;
    font-family: "Roboto", sans-serif;
    font-size: 10.5px;
    line-height: 1.5;
    color: var(--ink-light);
  }
  .terms-link {
    color: var(--accent-pink);
    font-weight: 500;
  }
</style>
</head>
<body>
  <main class="canvas">
    <section class="card card--front" aria-label="Gutschein Vorderseite">
      <h1 class="front-title">GUTSCHEIN</h1>
    </section>

    <section class="card card--back" aria-label="Gutschein Rückseite">
      <div class="brand">
        <span class="brand-dot"></span>
        <span class="brand-name">Feldring Atelier</span>
      </div>

      <div class="fields">
        <div class="field">Betrag :</div>
        <div class="field">Gültig Bis :</div>
        <div class="field">Code :</div>
      </div>

      <p class="terms">
        Diese Karte ist gültig nur auf der online shop seite <span class="terms-link">www.feldring-atelier.example</span> und in unserer offizielen Stores. Dieses Karte ist nicht<br>
        gültig bei rabatierte Produkten und man kann nicht mit dieser karte einen Gutscheinkarte kaufen.
      </p>
    </section>
  </main>
</body>
</html>
```